Business Card Design

Online clothing womens clothing store, I sell my clothing online and at the markets.

i would like the attached picture on the front of the card and the contact information on the back.

Industry/Entity Type

Business

Contact Information for Business Card

Harbor Thistle
Maren Pilcott
(Instagram symbol) _harbor_thistle_
(Facebook symbol) www.facebook.com/harborthistleau/

W : www.harborthistle.com.au
E : info@harborthistle.com.au
P : 0478614203

```html
<!DOCTYPE html>
<html lang="en">
<head>
<meta charset="utf-8">
<title>Harbor Thistle – Business Card</title>
<link href="https://fonts.googleapis.com/css2?family=Lato:wght@300;400;700;900&display=swap" rel="stylesheet">
<style>
  :root {
    --backdrop: #2b2b2b;
    --card-white: #f4f4f4;
    --ink: #111111;
    --ink-soft: #555555;
    --band-dark: #3a3a3a;
    --band-mid: #8f8f8f;
    --photo-mist: #dfe4e4;
    --photo-teal: #a9c4c2;
    --photo-shadow: #3d3a40;
    --paper-text: #ffffff;
  }
  * { margin: 0; padding: 0; box-sizing: border-box; }
  html, body {
    width: 1200px; height: 997px; overflow: hidden;
    background: var(--backdrop);
    font-family: "Lato", sans-serif;
  }
  .stage {
    position: relative; width: 1200px; height: 997px;
    display: flex; flex-direction: column; align-items: center; justify-content: center; gap: 44px;
  }
  .card {
    position: relative; width: 640px; height: 366px; overflow: hidden;
    box-shadow: 0 10px 30px rgba(0,0,0,.5);
  }
  /* Front */
  .card-front__photo {
    position: absolute; inset: 0;
    background:
      radial-gradient(ellipse 38% 55% at 66% 28%, var(--photo-shadow) 0%, rgba(61,58,64,.55) 45%, rgba(61,58,64,0) 78%),
      linear-gradient(160deg, var(--photo-teal) 0%, var(--photo-mist) 45%, #eef0f0 100%);
  }
  .card-front__name {
    position: absolute; left: 32px; bottom: 40px;
    color: var(--paper-text); font-weight: 700; font-size: 46px;
    letter-spacing: 5px; text-transform: uppercase; white-space: nowrap;
  }
  /* Back */
  .card-back { background: var(--card-white); color: var(--ink); }
  .brand { position: absolute; top: 44px; left: 0; right: 0; text-align: center; }
  .brand__name { font-weight: 300; font-size: 30px; letter-spacing: 9px; text-transform: uppercase; }
  .brand__url { margin-top: 4px; font-size: 11px; letter-spacing: 6px; color: var(--ink-soft); }
  .holder { position: absolute; top: 122px; left: 330px; width: 280px; }
  .holder__name { font-weight: 900; font-size: 22px; text-transform: uppercase; white-space: nowrap; }
  .holder__rule { display: flex; align-items: center; gap: 8px; margin-top: 4px; }
  .holder__rule span { flex: 1; height: 2px; background: var(--ink); }
  .holder__role { font-size: 13px; font-weight: 300; font-style: normal; color: var(--ink-soft); }
  .rule { position: absolute; height: 2px; background: var(--ink); }
  .rule--mid { top: 204px; left: 40px; width: 290px; }
  .rule--low { top: 262px; left: 40px; width: 250px; }
  .social { position: absolute; top: 192px; left: 340px; list-style: none; }
  .contact { position: absolute; top: 278px; left: 40px; list-style: none; }
  .social li, .contact li {
    display: flex; align-items: center; gap: 10px; font-size: 15px; height: 28px; white-space: nowrap;
  }
  .contact li svg { flex: 0 0 auto; width: 18px; }
  .marker { width: 14px; height: 14px; border: 2px solid var(--ink); border-radius: 3px; flex: 0 0 auto; }
  .band {
    position: absolute; right: 0; bottom: 0;
  }
  .band--tab {
    width: 150px; height: 118px; background: var(--band-mid); border-top-left-radius: 30px;
  }
  .band--foot {
    width: 100%; height: 12px; background: var(--band-dark);
  }
</style>
</head>
<body>
<main class="stage">
  <section class="card card-front">
    <div class="card-front__photo" role="img" aria-label="Misty teal-grey photograph of a windswept figure filling the card front"></div>
    <p class="card-front__name">Harbor Thistle</p>
  </section>

  <section class="card card-back">
    <div class="band band--tab"></div>
    <div class="band band--foot"></div>
    <header class="brand">
      <p class="brand__name">Harbor Thistle</p>
      <p class="brand__url">www.harborthistle.com.au</p>
    </header>
    <div class="holder">
      <p class="holder__name">Maren Pilcott</p>
      <div class="holder__rule"><span></span><em class="holder__role">Owner</em></div>
    </div>
    <div class="rule rule--mid"></div>
    <ul class="social">
      <li><i class="marker"></i>_harbor_thistle_</li>
      <li><i class="marker"></i>friendwall.net/harborthistle</li>
    </ul>
    <div class="rule rule--low"></div>
    <ul class="contact">
      <li>
        <svg width="18" height="20" viewBox="0 0 18 20" aria-hidden="true"><rect x="3" y="1" width="12" height="18" rx="2" fill="none" stroke="#111" stroke-width="2"/><line x1="7" y1="16" x2="11" y2="16" stroke="#111" stroke-width="1.5"/></svg>
        0478614203
      </li>
      <li>
        <svg width="18" height="13" viewBox="0 0 18 13" aria-hidden="true"><rect x="1" y="1" width="16" height="11" fill="none" stroke="#111" stroke-width="1.6"/><polyline points="1,1 9,7 17,1" fill="none" stroke="#111" stroke-width="1.6"/></svg>
        info@harborthistle.com.au
      </li>
    </ul>
  </section>
</main>
</body>
</html>
```